General Dental Office Business Card

I run a private general dental office in southern California, and would like a refresh/redesign of my business card. I focus on quality care rather than volume. The email address on the uploaded current card should be updated to: info@marbleshoredental.example. The current card's logo is a deboss, but I am open to other ideas. The logo can be refreshed, but it is something that's been with me since the beginning of the office, so I wouldn't want a drastic redesign.
Target Market(s)
Adults 18-99, whoever needs dental services
Industry/Entity Type
Healthcare/Dental
Contact Information for Business Card
Name, Address, Phone, email
Colors
Designer to choose colors to be used in the design.
Requirements
Must have
- Logo (Same as original one in the uploaded file), space on back for appointment time/date

```html
<!DOCTYPE html>
<html lang="en">
<head>
<meta charset="utf-8">
<title>Marble Shore Dental – Business Card</title>
<link rel="stylesheet" href="https://fonts.googleapis.com/css2?family=Open+Sans:wght@300;400;600;700&display=swap">
<style>
  :root {
    --bg: #2a2a2c;
    --card: #161616;
    --sky: #87d3ec;
    --white: #ffffff;
    --emboss: #2b2b2b;
    --emboss-text: #444444;
  }
  * { box-sizing: border-box; margin: 0; padding: 0; }
  html, body { width: 1200px; height: 1108px; overflow: hidden; }
  body {
    background: var(--bg);
    font-family: "Open Sans", sans-serif;
    color: var(--white);
    position: relative;
  }
  .card {
    position: absolute;
    top: 214px;
    width: 400px;
    height: 680px;
    background: var(--card);
    border-radius: 28px;
    overflow: hidden;
  }
  .card--front { left: 150px; }
  .card--back { left: 650px; }

  /* Front */
  .practice-vertical {
    position: absolute;
    left: 26px;
    top: 40px;
    writing-mode: vertical-rl;
    font-size: 54px;
    font-weight: 400;
    color: var(--sky);
    letter-spacing: 1px;
    line-height: 1;
  }
  .doctor {
    position: absolute;
    right: 40px;
    top: 46px;
    text-align: right;
  }
  .doctor__name { font-size: 25px; font-weight: 700; color: var(--sky); line-height: 1.2; }
  .doctor__title { font-size: 16px; font-weight: 400; letter-spacing: .5px; }
  .accent-bar {
    position: absolute;
    right: 0; top: 72px;
    width: 14px; height: 56px;
    background: var(--sky);
  }
  .mark-front {
    position: absolute;
    left: 130px; top: 220px;
    width: 210px; height: 210px;
    border-radius: 50%;
    border: 10px solid var(--emboss);
    display: flex; align-items: center; justify-content: center;
    text-align: center;
    font-size: 20px; font-weight: 600; color: var(--emboss-text);
    line-height: 1.3;
  }
  .contact {
    position: absolute;
    right: 36px; bottom: 40px;
    text-align: right;
    font-size: 15px;
    line-height: 1.45;
  }
  .contact__address { margin-bottom: 10px; }
  .contact__row { display: flex; justify-content: flex-end; align-items: center; gap: 8px; }
  .contact__row svg { width: 15px; height: 15px; flex: none; }

  /* Back */
  .field {
    position: absolute;
    left: 40px; right: 40px;
    border-top: 1.5px solid var(--white);
    text-align: center;
    font-size: 19px; font-weight: 600;
    padding-top: 10px;
    letter-spacing: .5px;
  }
  .field--date { top: 66px; }
  .field--time { top: 176px; }
  .mark-back {
    position: absolute;
    left: 110px; top: 290px;
    width: 190px; height: 190px;
    border-radius: 50%;
    background: var(--sky);
    display: flex; align-items: center; justify-content: center;
    text-align: center;
    color: var(--card);
    font-size: 20px; font-weight: 600; line-height: 1.3;
  }
  .wave-area {
    position: absolute;
    left: 0; right: 0;
    top: 492px; height: 80px;
    background: linear-gradient(to bottom, rgba(135,211,236,0.15), rgba(135,211,236,0.45));
  }
  .band {
    position: absolute;
    left: 0; bottom: 0;
    width: 400px; height: 120px;
  }
  .band-name {
    position: absolute;
    left: 0; right: 0; bottom: 40px;
    text-align: center;
    font-size: 36px; font-weight: 400;
    color: var(--white);
  }
</style>
</head>
<body>
  <section class="card card--front">
    <div class="practice-vertical">Marble Shore Dental</div>
    <div class="doctor">
      <div class="doctor__name">Daniel R. Park DDS</div>
      <div class="doctor__title">General Dentistry</div>
    </div>
    <div class="accent-bar"></div>
    <div class="mark-front">Marble<br>Shore<br>Dental</div>
    <div class="contact">
      <div class="contact__address">2180 Harbor Crest Way<br>Costa Verde, CA 92700</div>
      <div class="contact__row">555-014-2828
        <svg viewBox="0 0 16 16"><path d="M4 1.5l2.3 3-1.4 1.6c.9 2 2.4 3.5 4.4 4.4l1.6-1.4 3 2.3-1.2 2.6C7 14 2 9 1.5 2.7z" fill="#87d3ec"/></svg>
      </div>
      <div class="contact__row">info@marbleshoredental.example
        <svg viewBox="0 0 16 16"><rect x="1" y="3.5" width="14" height="9" rx="1" fill="none" stroke="#87d3ec" stroke-width="1.5"/><path d="M1.5 4l6.5 5 6.5-5" fill="none" stroke="#87d3ec" stroke-width="1.5"/></svg>
      </div>
      <div class="contact__row">www.marbleshoredental.example
        <svg viewBox="0 0 16 16"><circle cx="8" cy="8" r="6.5" fill="none" stroke="#87d3ec" stroke-width="1.5"/><path d="M1.5 8h13M8 1.5c-3 3.5-3 9.5 0 13M8 1.5c3 3.5 3 9.5 0 13" fill="none" stroke="#87d3ec" stroke-width="1.2"/></svg>
      </div>
    </div>
  </section>

  <section class="card card--back">
    <div class="field field--date">Appointment Date</div>
    <div class="field field--time">Time</div>
    <div class="mark-back">Marble<br>Shore<br>Dental</div>
    <div class="wave-area" role="img" aria-label="Decorative wave pattern in sky blue above the name band"></div>
    <svg class="band" viewBox="0 0 400 120" preserveAspectRatio="none">
      <path d="M0 8 C120 -4 260 16 400 28 V120 H0 Z" fill="#87d3ec"/>
    </svg>
    <div class="band-name">Marble Shore Dental</div>
  </section>
</body>
</html>
```